Kip Moor! Then Where?, Bail Bond Company Check-in App , Court date, Court Reminders, Payments

Kip Moor!
Then Where?
WINNER OF THIS CONTEST WILL HAVE OPPORTUNITY TO DESIGN CUSTOMIZE SOME OUR COMPANY PAGES AFTER CONTEST!
Check-in with your Bail agent via pic/video
Receive Court reminders
Make a payments

Basically this app is a portal to 3rd party bail companies.
The idea is for the person whom makes bail downloads the KipMoor app from Plaza Shelf.
Then they select a bail bond company.
This would be similar to a restaurant, real estate agent, insurance agent,,app where we could populate bail bond companies by client location or by typing in name of bail company.
We would like the ability to customize each bail bond company landing pages but are open to a global concept. when you click the bail bond company location it would have the logos for that company so the bail bond company screens would need to be customizeble
The app will require a photo or video check-in that is date and time
stamped with a gps location stored in check-in history
Check-in can be scheduled or random or voluntary
Voluntary and Scheduled Check-ins would require check-in button
Random would be via alert or text

The app should be able to receive court date updates
The app should allow clients to make payments to bail bond company
we need
KIP MOOR! landing page
client registration screens, check-in screens, available bail bond company screens for client to choose from
client registration page should include
name
email address
phone number
picture
home address
work address
date of birth
this app is different from our z-lumo app. this is a bail bond check-in app for third party bail bond companies.
landing page should be KIP MOOR! Then Where?
KIP MOOR ! Registration
Find your bail bond Company should list bail bond companies near me and search bar for searching bail bond companies by name
Next landing pages would be customizable for the third party bail bond companies
these would include pages for
check-ins via pics/videos
payment page
court reminders
contact information for bail bond companies
Kip Moor Pages include
initial landing page
registration page
search bail companies

Bail bond company pages should include
Bali bond company landing page
Use ORVAL BAIL BOND COMPANY as example
contact information for bail company
check-in page
payment page
court reminder page

Low designer entries

Low designer entries

Sick

Sick

Sick

Target Market(s)

Court Defendants, Probation ,jails, sheriffs, judges, attorneys

Industry/Entity Type

justice, law enforcement, courts,

Requirements
Must have
• Check-in via pic/video, ability to receive court date reminders, make paymentswe need client registration screens, check-in screens, available bail bond company screens for client to choose from
Nice to have
• Professional easy to navigate intuitive customizable to 3rd party bail bond companies, logos,phone numbers etc.
Should not have
• unprofessional graphics,

```html
<!DOCTYPE html>
<html lang="en">
<head>
<meta charset="utf-8">
<title>Quil Fen – Landing</title>
<link rel="stylesheet" href="https://fonts.googleapis.com/css2?family=Playfair+Display:wght@700&family=Poppins:wght@400&display=swap">
<style>
  :root {
    --bg-deep: #141516;
    --bg-mid: #2a2c2e;
    --bg-light: #3a3d40;
    --text-light: #ffffff;
  }
  * { margin: 0; padding: 0; box-sizing: border-box; }
  html, body {
    width: 1200px;
    height: 2594px;
    overflow: hidden;
    background: var(--bg-deep);
  }
  .landing-screen {
    position: relative;
    width: 1200px;
    height: 2594px;
    overflow: hidden;
  }
  .landing-backdrop {
    position: absolute;
    inset: 0;
    background:
      radial-gradient(ellipse 80% 40% at 60% 30%, var(--bg-light) 0%, transparent 70%),
      radial-gradient(ellipse 70% 30% at 40% 75%, var(--bg-mid) 0%, transparent 70%),
      linear-gradient(180deg, #1c1d1f 0%, var(--bg-mid) 35%, #1e2022 60%, var(--bg-deep) 100%);
  }
  .brand-block {
    position: absolute;
    left: 0;
    right: 0;
    top: 1180px;
    text-align: center;
    color: var(--text-light);
  }
  .brand-title {
    font-family: "Playfair Display", serif;
    font-weight: 700;
    font-size: 196px;
    line-height: 1;
    letter-spacing: -1px;
    white-space: nowrap;
  }
  .brand-tagline {
    margin-top: 26px;
    font-family: "Poppins", sans-serif;
    font-weight: 400;
    font-size: 50px;
    line-height: 1.2;
    white-space: nowrap;
  }
</style>
</head>
<body>
  <main class="landing-screen">
    <div class="landing-backdrop" role="img" aria-label="Dark photograph of prison bar shadows falling across a concrete floor"></div>
    <div class="brand-block">
      <h1 class="brand-title">Quil Fen</h1>
      <p class="brand-tagline">Online Quil Fen Management</p>
    </div>
  </main>
</body>
</html>
```